Inspirational ezine for girls aged 7-10

We need an ezine design to share a journal of life skills with girls of 7-10 years. It needs 28 pages which is developed with an opensource so it can be edited by other people. InDesign eBook is ok.

Design should be heartwarming, inspirational and hip (no princesses or fairies). See scan of mock-up and photos for ideas of layout and images (just examples from the web so don't use these directly).

Project Deadline Extended Reason: Hello,Extension due to a mis-categorisation as a flyer rather than a magazine. Only one design receivd so far!I have used ArtMarquee on several occasions and am happy to guarentee the payment once I'm sure that the ezine format can be provided. I haven't seen many on the site!All the best,Lorna Added Thursday, February 4, 2016

Girls aged 7-10

• Please see mock-up of pages attached (page 1 front cover, page 2 is an explanation, page 3 is customisable to add a photo and words of dedication, page 4 and 5 are on one side a title and an explanation and on the other side space to write so please show 3 sections with a title and then plain lines underneath). Ok t show dummy text for the moment.
• Front cover title : Navigating life, relationships and other important stuff...

```html
<!DOCTYPE html>
<html lang="en">
<head>
<meta charset="utf-8">
<title>Nature loves you – pages 17–18</title>
<link rel="stylesheet" href="https://fonts.googleapis.com/css2?family=Federo&family=Marcellus&family=Lato:wght@300&display=swap">
<style>
  :root {
    --paper: #f8ebe0;
    --teal: #7fd2c9;
    --pink-head: #ee8585;
    --pink-body: #f19a93;
    --peach: #f9c9ad;
    --peach-faint: #f6d8c8;
    --rose: #ec7aa6;
  }
  html, body {
    margin: 0;
    padding: 0;
    width: 1200px;
    height: 849px;
    overflow: hidden;
    background: var(--paper);
  }
  .spread {
    position: relative;
    width: 1200px;
    height: 849px;
    background: var(--paper);
    overflow: hidden;
  }
  .page {
    position: absolute;
    top: 0;
    width: 600px;
    height: 849px;
  }
  .page--left { left: 0; }
  .page--right { left: 600px; }

  .illustration-floral {
    position: absolute;
    inset: 0;
    background:
      radial-gradient(ellipse 42% 40% at 58% 46%, var(--paper) 0%, var(--paper) 55%, rgba(248,235,224,0) 100%),
      radial-gradient(circle at 10% 15%, #f6c95a 0%, rgba(246,201,90,0) 35%),
      radial-gradient(circle at 35% 5%, #f06c6c 0%, rgba(240,108,108,0) 35%),
      radial-gradient(circle at 5% 55%, #5ec8b5 0%, rgba(94,200,181,0) 35%),
      radial-gradient(circle at 15% 85%, #ef5e7e 0%, rgba(239,94,126,0) 40%),
      radial-gradient(circle at 90% 90%, #4ec2bd 0%, rgba(78,194,189,0) 35%),
      radial-gradient(circle at 55% 95%, #ee6f8f 0%, rgba(238,111,143,0) 35%),
      var(--paper);
  }
  .title {
    position: absolute;
    left: 176px;
    top: 340px;
    margin: 0;
    font-family: "Federo", sans-serif;
    font-weight: 400;
    font-size: 52px;
    color: var(--teal);
    letter-spacing: -0.5px;
    white-space: nowrap;
  }

  .decor-bird-left {
    position: absolute;
    left: 0;
    top: 690px;
    width: 82px;
    height: 159px;
    background: var(--peach);
    border-radius: 0 60% 0 0;
  }
  .decor-bird-right {
    position: absolute;
    left: 448px;
    top: 732px;
    width: 152px;
    height: 117px;
    background: var(--rose);
    border-radius: 70% 0 0 0;
  }
  .page-number {
    position: absolute;
    font-family: "Marcellus", serif;
    font-size: 20px;
    color: #5a4a55;
  }
  .page-number--left { left: 32px; top: 776px; }
  .page-number--right { left: 520px; top: 786px; }

  .decor-paisley {
    position: absolute;
    left: 308px;
    top: 36px;
    width: 264px;
    height: 428px;
    background: radial-gradient(ellipse at 50% 60%, var(--peach-faint) 0%, rgba(246,216,200,0.35) 70%, rgba(246,216,200,0) 100%);
    border-radius: 50% 50% 50% 50% / 40% 40% 60% 60%;
  }

  .article {
    position: absolute;
    left: 104px;
    top: 356px;
    width: 420px;
  }
  .article__heading {
    margin: 0 0 26px;
    font-family: "Marcellus", serif;
    font-weight: 400;
    font-size: 22px;
    line-height: 26px;
    color: var(--pink-head);
  }
  .article__lead,
  .article__text {
    font-family: "Lato", sans-serif;
    font-weight: 300;
    font-size: 12.2px;
    line-height: 18.4px;
    margin: 0 0 18px;
  }
  .article__lead { color: var(--teal); }
  .article__text { color: var(--pink-body); }
</style>
</head>
<body>
<main class="spread">
  <section class="page page--left">
    <div class="illustration-floral" role="img" aria-label="Watercolour wash with hand-drawn flowers, leaves and two lace butterflies framing the title"></div>
    <h1 class="title">Nature loves you</h1>
    <div class="decor-bird-left" role="img" aria-label="Peach bird silhouette"></div>
    <span class="page-number page-number--left">17.</span>
  </section>

  <section class="page page--right">
    <div class="decor-paisley" role="img" aria-label="Faint patterned paisley bird ornament"></div>
    <article class="article">
      <h2 class="article__heading">Treat nature like a friend,<br>with kindness and respect.</h2>
      <p class="article__lead">A healthy environment is ressourcing.</p>
      <p class="article__text">How does it make you feel to be by the sea ?<br>
        Or in a beautiful green field surrounded by flowers ?<br>
        Near animals ?<br>
        High up in snowy mountains ?<br>
        Does it help you to feel full of energy ?<br>
        Or so calm and content that you feel like sleeping ?</p>
      <p class="article__text">Our big cities are full of pollution and noise. Take time outto be surrounded by the beautiful gifts nature shares with us. We can find calm by just breathing in and out and sitting calmly.</p>
      <p class="article__text">We can say thank you to nature by being careful in our daily activities, by recycling, eating less meat, creating less waste. If everyone helps a little bit by being responsible thne our small actions can have a big impact in helping all of nature to stay clean enough to support us.</p>
    </article>
    <div class="decor-bird-right" role="img" aria-label="Pink bird silhouette in flight"></div>
    <span class="page-number page-number--right">18.</span>
  </section>
</main>
</body>
</html>
```